Plumbing business card and logo desgin

Need a new business card and logo for a plumbing business based in Warragul, Australia. Business name is 7Kelby plumbing & air-conditioning. We service all plumbing and gasfitting needs and installation of air-conditioning. We clear blocked drains, install new hot water systems, central heating, new and existing homes, roofing, sanitary and drainage.
i would like to have a space on there for website, email, phone, licence number and what we do as a company.
i would like a water droplet to be incorporated into the design to try and stand out that we are a plumbing business

Contact Information for Business Card

website:
phone number: 0458271936
Licence Number: 382716

Logo Text

7Kelby Plumbing & Air-Conditioning

```html
<!DOCTYPE html>
<html lang="en">
<head>
<meta charset="utf-8">
<title>7Kelby Plumbing &amp; Air-Conditioning — Business Card</title>
<link rel="stylesheet" href="https://fonts.googleapis.com/css2?family=Montserrat:wght@700&family=Questrial&display=swap">
<style>
  :root {
    --page: #eceef2;
    --card: #f4f5f7;
    --brand-blue: #1b6fbd;
    --deep-blue: #1f48a8;
    --sky-blue: #27a6e3;
    --ink: #333a44;
    --band-lavender: #c6d0e8;
    --band-pale: #e6e9f2;
    --white: #ffffff;
  }
  * { margin: 0; padding: 0; box-sizing: border-box; }
  html, body { width: 1131px; height: 1200px; overflow: hidden; }
  body {
    background: var(--page);
    position: relative;
    font-family: "Questrial", "Century Gothic", sans-serif;
    color: var(--ink);
  }
  .card {
    position: absolute;
    left: 177px;
    width: 777px;
    height: 444px;
    border-radius: 22px;
    background: var(--card);
    overflow: hidden;
    box-shadow: 0 14px 24px rgba(0,0,0,0.18);
  }
  .card--front { top: 103px; }
  .card--back { top: 615px; }

  .front-texture {
    position: absolute; inset: 0;
    background: radial-gradient(circle at 70% 40%, #fbfcfd 0%, #eef0f4 60%, #e6e9ee 100%);
  }
  .brand {
    position: absolute; left: 55px; top: 78px;
  }
  .brand__name {
    font-family: "Questrial", sans-serif;
    font-size: 76px;
    line-height: 1;
    color: var(--brand-blue);
    letter-spacing: 1px;
  }
  .brand__tagline {
    font-size: 22px;
    color: var(--ink);
    margin-top: 6px;
    margin-left: 4px;
  }
  .contact {
    position: absolute; left: 46px; top: 294px;
    list-style: none;
    font-size: 23px;
    line-height: 32px;
  }
  .contact__label { margin-right: 8px; }
  .contact .accent { color: var(--brand-blue); }
  .front-band {
    position: absolute; left: 0; bottom: 0; width: 777px; height: 32px;
  }
  .licence {
    position: absolute; right: 40px; bottom: 3px;
    color: var(--white);
    font-size: 22px;
    letter-spacing: 0.5px;
  }

  .services__title {
    position: absolute; left: 50px; top: 44px;
    font-family: "Montserrat", sans-serif;
    font-weight: 700;
    font-size: 49px;
    color: var(--brand-blue);
    letter-spacing: 0.5px;
  }
  .services__list {
    position: absolute; left: 46px; top: 118px;
    list-style: none;
    font-size: 23px;
    line-height: 33.5px;
    z-index: 2;
  }
  .services__list li { display: flex; align-items: center; }
  .services__list li::before {
    content: "";
    width: 13px; height: 13px; border-radius: 50%;
    background: var(--brand-blue);
    margin-right: 18px;
  }
  .back-bands { position: absolute; inset: 0; }
  .brand-mark {
    position: absolute; left: 452px; top: 62px;
    width: 300px; height: 300px; border-radius: 50%;
    background: var(--brand-blue);
  }
</style>
</head>
<body>
  <section class="card card--front">
    <div class="front-texture" role="img" aria-label="Background of scattered clear water droplets"></div>
    <div class="brand">
      <div class="brand__name">7Kelby</div>
      <div class="brand__tagline">Plumbing &amp; Air-Conditioning</div>
    </div>
    <ul class="contact">
      <li><span class="contact__label">P:</span>0458271936</li>
      <li><span class="contact__label">m:</span>hello@7kelbyplumbing.com</li>
      <li><span class="contact__label">w:</span>www.<span class="accent">7kelbyplumbing</span>.com</li>
    </ul>
    <svg class="front-band" viewBox="0 0 777 32" preserveAspectRatio="none" aria-hidden="true">
      <defs>
        <linearGradient id="bandDeep" x1="0" x2="1">
          <stop offset="0" stop-color="#1f3fa3"/>
          <stop offset="1" stop-color="#2a6cc4"/>
        </linearGradient>
        <linearGradient id="bandSky" x1="0" x2="1">
          <stop offset="0" stop-color="#2a6cc4"/>
          <stop offset="1" stop-color="#27a6e3"/>
        </linearGradient>
      </defs>
      <polygon points="0,0 391,0 369,32 0,32" fill="url(#bandDeep)"/>
      <polygon points="398,0 777,0 777,32 376,32" fill="url(#bandSky)"/>
    </svg>
    <div class="licence">Licence No: 382716</div>
  </section>

  <section class="card card--back">
    <svg class="back-bands" viewBox="0 0 777 444" preserveAspectRatio="none" aria-hidden="true">
      <polygon points="0,444 445,267 777,267 777,388 0,388" fill="var(--band-lavender)"/>
      <rect x="0" y="388" width="777" height="56" fill="var(--band-pale)"/>
      <polygon points="0,444 140,388 0,388" fill="var(--band-pale)"/>
    </svg>
    <div class="brand-mark" aria-hidden="true"></div>
    <h2 class="services__title">OUR SERVICE</h2>
    <ul class="services__list">
      <li>installation of air-conditioning</li>
      <li>install new hot water systems</li>
      <li>plumbing and gasfitting</li>
      <li>new and existing homes</li>
      <li>sanitary and drainage</li>
      <li>clear blocked drains</li>
      <li>central heating</li>
      <li>roofing</li>
    </ul>
  </section>
</body>
</html>
```